Epoxy coatings company needs a logo/business card design.

My company name is "Meridian Resin Works", and I am looking for a company logo and business card design.
My initial thought was to use "Æ"in 'Oe'sthetic, and would also like to see ideas on how to play around with the fact that the first 3 letters (Mer) are also the acronym of the company name.
I specialize in garage floor and interior epoxy coatings, paint flake broadcasts, quartz broadcasts, and solid color epoxy floors, concrete repairs.
I like images I've seen of a silhouetted person running a floor grinder. It keeps the design of the card simple. I'm not necessarily opposed to using images of the floors on the card, but I'd prefer to keep the front simple (Company name, my name, phone number, email) and maybe put pictures on the back. I've included a few of my personal pictures of floors I've done (including a before, after, and when the garage was being used after)
My colors are darker green (Fern/Forest/Hunter, etc), and Bronze.

Contact Information for Business Card

Name: Dana Kolvesky Email: meridianresinworks@plinkmail.test Phone: (555)318-2964 Instagram: meridian_resin_works

Colors

Designer to choose colors to be used in the design.

Requirements
Nice to have
• I've included a business card designed for someone else, that contains the silhouette that I'm looking for. The floor grinder that I use is large like the one pictured (Torvex G40R).

```html
<!DOCTYPE html>
<html lang="en">
<head>
<meta charset="utf-8">
<title>Meridian Resin Works — Business Card</title>
<link href="https://fonts.googleapis.com/css2?family=Montserrat:wght@300;700&family=Roboto:wght@400;700&display=swap" rel="stylesheet">
<style>
  :root {
    --forest: #0c3322;
    --forest-deep: #082a1b;
    --bronze: #c9843a;
    --paper: #ffffff;
    --ghost: #f2efea;
    --stage: #3a3a3c;
    --ink: #0c3322;
  }
  * { margin: 0; padding: 0; box-sizing: border-box; }
  html, body { width: 1200px; height: 960px; overflow: hidden; }
  body {
    background: var(--stage);
    font-family: "Roboto", Arial, sans-serif;
    position: relative;
  }
  .card {
    position: absolute;
    left: 220px;
    width: 760px;
    height: 434px;
    overflow: hidden;
    box-shadow: 0 10px 30px rgba(0,0,0,.45);
  }
  /* Back side */
  .card-back { top: 30px; background: var(--forest); }
  .back-brand {
    position: absolute; left: 0; right: 0; top: 62px;
    display: flex; align-items: center; justify-content: center; gap: 22px;
  }
  .brand-mark { width: 64px; height: 64px; background: var(--bronze); }
  .back-brand .brand-name {
    font-family: "Montserrat", Arial, sans-serif;
    font-weight: 700; font-size: 54px; color: var(--bronze);
    text-transform: uppercase; letter-spacing: 1px;
  }
  .project-gallery {
    position: absolute; left: 60px; right: 60px; top: 210px;
    display: flex; justify-content: space-between;
  }
  .project-photo {
    width: 196px; height: 160px;
    border: 7px solid var(--bronze);
  }
  .photo-before { background: linear-gradient(160deg, #c9c9c4, #8d8c86); }
  .photo-after { background: linear-gradient(160deg, #a7abb2, #5c616b); }
  .photo-in-use { background: linear-gradient(160deg, #6b6458, #8f949a 60%, #b9bcc0); }

  /* Front side */
  .card-front { top: 496px; background: var(--paper); }
  .ghost-square {
    position: absolute; left: 510px; top: 24px;
    width: 200px; height: 200px; background: var(--ghost);
  }
  .divider-line {
    position: absolute; left: 340px; top: 236px;
    width: 400px; height: 1px; background: var(--bronze);
  }
  .front-brand {
    position: absolute; left: 40px; top: 100px;
    display: flex; align-items: center; gap: 14px;
  }
  .front-brand .brand-mark { width: 40px; height: 40px; background: var(--forest); }
  .front-brand .brand-name {
    font-family: "Montserrat", Arial, sans-serif;
    font-weight: 700; font-size: 26px; color: var(--forest);
    text-transform: uppercase; letter-spacing: .5px;
  }
  .contact { position: absolute; left: 40px; top: 246px; }
  .person-name {
    font-weight: 700; font-size: 30px; color: var(--ink);
    padding-bottom: 12px; border-bottom: 1px solid var(--bronze);
    width: 270px;
  }
  .contact-list { list-style: none; margin-top: 10px; }
  .contact-list li {
    display: flex; align-items: center; gap: 10px;
    color: var(--bronze); font-size: 17px; line-height: 28px;
  }
  .contact-list svg { width: 14px; height: 14px; flex: none; }
  .band { position: absolute; left: 0; top: 0; width: 760px; height: 434px; }
</style>
</head>
<body>
  <section class="card card-back" aria-label="Card back">
    <div class="back-brand">
      <span class="brand-mark"></span>
      <span class="brand-name">Meridian Resin Works</span>
    </div>
    <div class="project-gallery">
      <div class="project-photo photo-before" role="img" aria-label="Photo of a bare concrete garage floor before coating"></div>
      <div class="project-photo photo-after" role="img" aria-label="Photo of a finished flake epoxy floor"></div>
      <div class="project-photo photo-in-use" role="img" aria-label="Photo of the coated garage in use with a parked car"></div>
    </div>
  </section>

  <section class="card card-front" aria-label="Card front">
    <div class="ghost-square"></div>
    <div class="divider-line"></div>
    <svg class="band" viewBox="0 0 760 434" aria-hidden="true">
      <path d="M0 390 L440 390 C480 390 482 342 522 342 L760 342 L760 434 L0 434 Z" fill="var(--bronze)"/>
      <path d="M0 400 L446 400 C486 400 488 352 528 352 L760 352 L760 434 L0 434 Z" fill="var(--forest)"/>
      <rect x="0" y="422" width="760" height="3" fill="var(--bronze)"/>
    </svg>
    <div class="front-brand">
      <span class="brand-mark"></span>
      <span class="brand-name">Meridian Resin Works</span>
    </div>
    <div class="contact">
      <p class="person-name">Dana Kolvesky</p>
      <ul class="contact-list">
        <li>
          <svg viewBox="0 0 14 14"><rect x="3" y="0.5" width="8" height="13" rx="1.5" fill="none" stroke="var(--ink)" stroke-width="1.2"/><rect x="6" y="11" width="2" height="1" fill="var(--ink)"/></svg>
          (555)318-2964
        </li>
        <li>
          <svg viewBox="0 0 14 14"><rect x="0.5" y="3" width="13" height="9" fill="var(--ink)"/><path d="M0.5 3 L7 8 L13.5 3" fill="none" stroke="#fff" stroke-width="1"/></svg>
          meridianresinworks@plinkmail.test
        </li>
      </ul>
    </div>
  </section>
</body>
</html>
```